Town Planning Consultants require lstationary design

Require a design to be used for our letterhead and report cover page. We have an approved logo.
we have attached our logo, and our temporary letterhead/cover page (SEE Cover) which we currently adapt for both purposes in the interim pending a permanent design. I have also attached an example (example report cover) of a report cover page that I like. perhaps similar with our colour scheme

Target Market(s)

?

Industry/Entity Type

Town

Colors
249fd4
3176b5

Requirements
Must have
• colours to match logo
• the text content in existing letterhead

```html
<!DOCTYPE html>
<html lang="en">
<head>
<meta charset="utf-8">
<title>Statement of Environmental Effects – Report Cover</title>
<link rel="stylesheet" href="https://fonts.googleapis.com/css2?family=Open+Sans:wght@400;600;700&display=swap">
<style>
  :root {
    --brand-blue: #3176b5;
    --brand-sky: #249fd4;
    --sky-light: #5cc3ec;
    --sky-pale: #8fd8f2;
    --navy: #1f4f8f;
    --ink: #222222;
    --paper: #ffffff;
    --photo-top: #c9d6ea;
    --photo-bottom: #b9cfd8;
  }
  * { box-sizing: border-box; margin: 0; padding: 0; }
  html, body { width: 848px; height: 1200px; overflow: hidden; background: var(--paper); }
  body { font-family: "Open Sans", Verdana, sans-serif; color: var(--ink); }
  .cover { position: relative; width: 848px; height: 1200px; overflow: hidden; background: var(--paper); }
  .decor { position: absolute; inset: 0; }

  .brand {
    position: absolute; left: 508px; top: 66px; height: 50px;
    display: flex; align-items: center; gap: 10px;
  }
  .brand-square { width: 22px; height: 22px; background: var(--brand-sky); }
  .brand-name { font-size: 38px; font-weight: 600; color: var(--brand-blue); letter-spacing: 0.5px; line-height: 50px; }

  .contact { position: absolute; top: 174px; font-size: 14px; line-height: 20px; color: var(--ink); }
  .contact-phone { left: 228px; }
  .contact-mobile { left: 402px; }
  .contact-address { left: 651px; }

  .report-title {
    position: absolute; top: 266px; left: 0; width: 848px; text-align: center;
    font-size: 31px; font-weight: 700; letter-spacing: 0.2px;
  }
  .report-subtitle { position: absolute; top: 314px; left: 166px; font-size: 25px; font-weight: 400; }

  .site-photo {
    position: absolute; left: 178px; top: 403px; width: 556px; height: 367px;
    background: linear-gradient(180deg, var(--photo-top) 0%, var(--photo-bottom) 100%);
    box-shadow: 0 0 0 2px #ffffff;
  }

  .site-address {
    position: absolute; top: 846px; left: 140px; display: flex; align-items: center; gap: 10px;
    font-size: 28px; font-weight: 700;
  }

  .meta { position: absolute; left: 60px; top: 920px; }
  .meta-labels, .meta-values { position: absolute; top: 0; font-size: 19px; line-height: 34.5px; white-space: nowrap; }
  .meta-labels { left: 0; }
  .meta-values { left: 172px; }
  .meta-rule { position: absolute; left: 154px; top: 4px; width: 4px; height: 143px; background: var(--brand-blue); border-radius: 2px; }

  .services { position: absolute; top: 1132px; left: 0; width: 848px; font-size: 20px; }
  .service { position: absolute; display: flex; align-items: center; gap: 4px; }
  .service svg { width: 26px; height: 26px; }
</style>
</head>
<body>
<main class="cover">
  <svg class="decor" width="848" height="1200" viewBox="0 0 848 1200" aria-hidden="true">
    <!-- header bands, stopping short of the company name -->
    <polygon points="262,34 490,34 490,84 300,84" fill="var(--sky-pale)"/>
    <polygon points="720,34 848,34 848,84 720,84" fill="var(--sky-pale)"/>
    <polygon points="112,62 490,62 490,116 148,116" fill="var(--brand-blue)"/>
    <polygon points="112,62 420,62 410,86 130,86" fill="var(--brand-sky)" opacity="0.55"/>
    <polygon points="172,122 848,122 848,158 200,158" fill="var(--sky-light)"/>
    <!-- photo surround -->
    <polygon points="382,359 848,359 848,627 382,627" fill="var(--sky-pale)"/>
    <polygon points="0,634 360,634 428,823 0,823" fill="var(--sky-light)"/>
    <rect x="147" y="382" width="608" height="416" fill="var(--brand-blue)"/>
    <rect x="147" y="382" width="608" height="120" fill="var(--brand-sky)" opacity="0.45"/>
    <rect x="147" y="770" width="608" height="28" fill="var(--navy)"/>
  </svg>

  <div class="brand">
    <span class="brand-square"></span>
    <span class="brand-name">Tidewell</span>
  </div>

  <p class="contact contact-phone">+61 (2) 5550&nbsp; 1234<br>hello@tidewell.com.au</p>
  <p class="contact contact-mobile">+61 (0)400 555018</p>
  <p class="contact contact-address">12 Harbour Ridge Road,<br>ELMSTONE&nbsp; NSW 2400</p>

  <h1 class="report-title">Statement of Environmental Effects</h1>
  <h2 class="report-subtitle">Proposed Additions to Existing Dwelling</h2>

  <div class="site-photo" role="img" aria-label="Photograph of the waterfront site seen from the river"></div>

  <div class="site-address">
    <svg width="34" height="44" viewBox="0 0 34 44" aria-hidden="true">
      <path d="M17 1 C8 1 1 8 1 17 C1 29 17 43 17 43 C17 43 33 29 33 17 C33 8 26 1 17 1 Z" fill="var(--brand-sky)"/>
      <circle cx="17" cy="16" r="6" fill="var(--paper)"/>
    </svg>
    <span>18 Marlow Avenue, KESTREL BAY</span>
  </div>

  <section class="meta">
    <p class="meta-labels">Prepared for<br><br>Reviewed by<br>Dated</p>
    <span class="meta-rule"></span>
    <p class="meta-values">M.Haldane<br>R.Calder<br>T. Morrow<br>June, 2016</p>
  </section>

  <nav class="services">
    <span class="service" style="left:56px">
      <svg viewBox="0 0 26 26" aria-hidden="true" fill="none" stroke="#555" stroke-width="1.6">
        <path d="M3 6 l2 2 l3 -4 M3 13 l2 2 l3 -4 M3 20 l2 2 l3 -4"/><path d="M11 7 h12 M11 14 h12 M11 21 h12"/>
      </svg>Planning</span>
    <span class="service" style="left:204px">
      <svg viewBox="0 0 26 26" aria-hidden="true" fill="#555">
        <circle cx="9" cy="15" r="6"/><circle cx="9" cy="15" r="2.2" fill="#fff"/>
        <circle cx="19" cy="8" r="4"/><circle cx="19" cy="8" r="1.5" fill="#fff"/>
      </svg>Development</span>
    <span class="service" style="left:412px">
      <svg viewBox="0 0 26 26" aria-hidden="true" fill="none" stroke="#555" stroke-width="1.6">
        <rect x="3" y="4" width="16" height="19" rx="1"/><path d="M9 18 L22 5 l2 2 L11 20 l-3 1 Z"/>
      </svg>Urban Design</span>
    <span class="service" style="left:616px">
      <svg viewBox="0 0 26 26" aria-hidden="true" fill="none" stroke="#555" stroke-width="1.8">
        <path d="M4 16 V12 a9 9 0 0 1 18 0 V16"/><rect x="3" y="13" width="4" height="7" rx="1.5"/><rect x="19" y="13" width="4" height="7" rx="1.5"/><path d="M21 20 q0 3 -6 3"/>
      </svg>Consultant</span>
  </nav>
</main>
</body>
</html>
```